Business Card Design Project

we are a new company , see www.chatharborlane.com
we also have a concurrent flyer deign competition so you may also wish to enter that.
We provide live customer support services for websites.
We cater for mainly european market.
info for card:
Martin Colbrook
Director
p: +353 (0)90 612 8051
f: +353 (0)90 612 8062
m: +353 (0)86 507 4926
e: martin@chatharborlane.com
w: www.chatharborlane.com
The card does not have to use the exact colour on the website but should ahve something of the general feel of it. It should have modern corporate feel without brash coulours. we will upload the logo and card should be standard european size 85x55mm
Target Market(s)
Online business owners
Industry/Entity Type
Business
Look and feel
Each slider illustrates characteristics of the customer's brand and the style your logo design should communicate.

```html
<!DOCTYPE html>
<html lang="en">
<head>
<meta charset="utf-8">
<title>Chat Harbor Lane — Business Card</title>
<link href="https://fonts.googleapis.com/css2?family=Arimo:wght@400;700&display=swap" rel="stylesheet">
<style>
  :root {
    --backdrop: #e7e5e2;
    --card-dark: #4b4b4d;
    --card-light: #ffffff;
    --accent-blue: #1c97d4;
    --text-grey: #555658;
    --text-soft: #d9d9d9;
    --logo-white: #ffffff;
  }
  * { margin: 0; padding: 0; box-sizing: border-box; }
  html, body { width: 1200px; height: 828px; overflow: hidden; }
  body {
    background: var(--backdrop);
    font-family: "Arimo", Arial, sans-serif;
    position: relative;
  }
  .card {
    position: absolute;
    top: 239px;
    width: 540px;
    height: 350px;
    border-radius: 26px;
    overflow: hidden;
    box-shadow: 0 10px 24px rgba(0,0,0,0.18);
  }
  .card-back { left: 40px; background: var(--card-dark); }
  .card-front { left: 620px; background: var(--card-light); }

  .brand {
    position: absolute;
    display: flex;
    align-items: center;
    gap: 12px;
    color: var(--logo-white);
    font-weight: 700;
    white-space: nowrap;
  }
  .brand-mark {
    background: var(--accent-blue);
    flex: none;
  }
  .card-back .brand { left: 50%; top: 50%; transform: translate(-50%, -60%); font-size: 38px; }
  .card-back .brand-mark { width: 30px; height: 30px; }
  .card-back .website {
    position: absolute;
    right: 40px;
    bottom: 34px;
    font-size: 14px;
    color: var(--text-soft);
  }

  .front-panel {
    position: absolute;
    left: 0; top: 0;
    width: 232px; height: 100%;
    background: var(--card-dark);
  }
  .front-notch {
    position: absolute;
    left: 231px;
    top: 88px;
    width: 16px;
    height: 26px;
  }
  .card-front .brand {
    left: 116px; top: 200px;
    transform: translate(-50%, -50%);
    font-size: 22px;
    gap: 8px;
  }
  .card-front .brand-mark { width: 18px; height: 18px; }

  .contact { position: absolute; left: 276px; top: 72px; }
  .contact-name { font-size: 22px; color: var(--accent-blue); line-height: 1.1; }
  .contact-role { font-size: 15px; color: var(--text-grey); margin-top: 4px; }
  .contact-list { list-style: none; margin-top: 30px; }
  .contact-list li {
    display: flex;
    font-size: 15px;
    line-height: 21px;
    color: var(--text-grey);
  }
  .contact-label { width: 20px; color: var(--accent-blue); }
</style>
</head>
<body>
  <section class="card card-back" aria-label="Card back">
    <div class="brand"><span class="brand-mark"></span>Chat Harbor Lane</div>
    <p class="website">www.chatharborlane.com</p>
  </section>

  <section class="card card-front" aria-label="Card front">
    <div class="front-panel"></div>
    <svg class="front-notch" viewBox="0 0 16 26" aria-hidden="true">
      <polygon points="0,0 16,13 0,26" fill="#4b4b4d"/>
    </svg>
    <div class="brand"><span class="brand-mark"></span>Chat Harbor Lane</div>

    <div class="contact">
      <h1 class="contact-name">Martin Colbrook</h1>
      <p class="contact-role">Director</p>
      <ul class="contact-list">
        <li><span class="contact-label">p</span>+353 (0)90 612 8051</li>
        <li><span class="contact-label">f</span>+353 (0)90 612 8062</li>
        <li><span class="contact-label">m</span>+353 (0)86 507 4926</li>
        <li><span class="contact-label">e</span>martin@chatharborlane.com</li>
        <li><span class="contact-label">w</span>www.chatharborlane.com</li>
      </ul>
    </div>
  </section>
</body>
</html>
```